Larvik Consulting

Hi,
I have my own network consulting business (just me)
and need to get a logo and business card design together,

Based in New Zealand,

Tobias Wrenfield
Unified Communications and Network Architect

/design engineer,
and would like this to be the basis for personal branding and company identity

Industry/Entity Type

Business

Requirements
Nice to have
• I have the basis for a optional logo - needs color -

```html
<!DOCTYPE html>
<html lang="en">
<head>
<meta charset="utf-8">
<title>Larvik Consulting — Business Card</title>
<link href="https://fonts.googleapis.com/css2?family=Jura:wght@400;500&display=swap" rel="stylesheet">
<style>
  :root {
    --backdrop: #e7e8ec;
    --card-white: #ffffff;
    --brand-blue: #2f6fd0;
    --panel-blue-light: #3257b8;
    --panel-blue-dark: #1c3896;
    --panel-glow: #4a7fd6;
    --text-on-blue: #ffffff;
    --text-soft: #a9c4f2;
    --shadow: rgba(20, 30, 60, 0.25);
  }
  * { margin: 0; padding: 0; box-sizing: border-box; }
  html, body {
    width: 1200px;
    height: 900px;
    overflow: hidden;
    background: var(--backdrop);
    font-family: "Jura", "Segoe UI", sans-serif;
  }
  .canvas {
    position: relative;
    width: 1200px;
    height: 900px;
  }

  /* Front of card */
  .card-front {
    position: absolute;
    left: 60px;
    top: 40px;
    width: 840px;
    height: 500px;
    display: flex;
    box-shadow: 0 6px 18px var(--shadow);
  }
  .front-brand {
    width: 378px;
    height: 100%;
    background: var(--card-white);
    display: flex;
    flex-direction: column;
    align-items: center;
    justify-content: center;
    gap: 34px;
  }
  .brand-name {
    color: var(--brand-blue);
    font-weight: 500;
    text-align: center;
    line-height: 1.1;
    letter-spacing: 0.08em;
  }
  .brand-name--front { font-size: 46px; }
  .brand-name--front span { display: block; font-size: 21px; letter-spacing: 0.42em; margin-top: 6px; }
  .brand-dot {
    width: 58px;
    height: 58px;
    border-radius: 50%;
    background: var(--brand-blue);
  }

  .front-details {
    position: relative;
    flex: 1;
    height: 100%;
    color: var(--text-on-blue);
    overflow: hidden;
  }
  .panel-texture {
    position: absolute;
    inset: 0;
    background:
      radial-gradient(ellipse 70% 55% at 30% 75%, var(--panel-glow) 0%, transparent 70%),
      linear-gradient(160deg, var(--panel-blue-light) 0%, var(--panel-blue-dark) 100%);
  }
  .holder {
    position: absolute;
    left: 52px;
    top: 128px;
  }
  .holder-name {
    font-size: 40px;
    font-weight: 500;
    letter-spacing: 0.03em;
  }
  .holder-role {
    font-size: 12.5px;
    color: var(--text-soft);
    letter-spacing: 0.04em;
    margin-top: 2px;
  }
  .address {
    position: absolute;
    left: 70px;
    top: 335px;
    font-size: 17px;
    color: var(--text-soft);
    letter-spacing: 0.03em;
  }
  .contact-list {
    position: absolute;
    left: 252px;
    top: 376px;
    list-style: none;
    font-size: 17px;
    color: var(--text-soft);
    letter-spacing: 0.03em;
  }
  .contact-list li {
    display: flex;
    align-items: center;
    gap: 10px;
    height: 25px;
  }
  .contact-icon {
    width: 16px;
    height: 16px;
    display: flex;
    align-items: center;
    justify-content: center;
    color: var(--text-on-blue);
    font-weight: 500;
    font-size: 17px;
  }
  .contact-icon svg { width: 16px; height: 16px; fill: var(--text-on-blue); }

  /* Back of card */
  .card-back {
    position: absolute;
    left: 580px;
    top: 570px;
    width: 540px;
    height: 300px;
    color: var(--text-on-blue);
    overflow: hidden;
    box-shadow: 0 6px 18px var(--shadow);
  }
  .back-brand {
    position: absolute;
    left: 0;
    right: 0;
    top: 96px;
    display: flex;
    align-items: center;
    justify-content: center;
    gap: 14px;
  }
  .brand-name--back {
    color: var(--text-on-blue);
    font-size: 26px;
  }
  .brand-dot--back {
    width: 26px;
    height: 26px;
    background: var(--text-on-blue);
  }
  .website {
    position: absolute;
    right: 36px;
    bottom: 22px;
    font-size: 11px;
    letter-spacing: 0.04em;
    color: var(--text-on-blue);
  }
</style>
</head>
<body>
<main class="canvas">

  <section class="card-front" aria-label="Business card, front">
    <div class="front-brand">
      <div class="brand-name brand-name--front">LARVIK<span>CONSULTING</span></div>
      <div class="brand-dot" aria-hidden="true"></div>
    </div>

    <div class="front-details">
      <div class="panel-texture" role="img" aria-label="Blue background with soft curved globe lines"></div>

      <div class="holder">
        <h1 class="holder-name">Tobias Wrenfield</h1>
        <p class="holder-role">Unified Communications and Network Architect</p>
      </div>

      <p class="address">Address: Street, state, zip, country</p>

      <ul class="contact-list">
        <li>
          <span class="contact-icon" aria-label="Phone">
            <svg viewBox="0 0 24 24"><path d="M6.6 10.8a15.1 15.1 0 0 0 6.6 6.6l2.2-2.2c.3-.3.7-.4 1-.2 1.1.4 2.3.6 3.6.6.6 0 1 .4 1 1V20c0 .6-.4 1-1 1C10.6 21 3 13.4 3 4c0-.6.4-1 1-1h3.5c.6 0 1 .4 1 1 0 1.3.2 2.5.6 3.6.1.3 0 .7-.2 1z"/></svg>
          </span>
          <span>021 - 485730</span>
        </li>
        <li>
          <span class="contact-icon" aria-label="Fax">F</span>
          <span>021 - 485731</span>
        </li>
        <li>
          <span class="contact-icon" aria-label="Email">
            <svg viewBox="0 0 24 24"><path d="M2 5h20v14H2z M4 7v.4l8 5.2 8-5.2V7zm0 2.8V17h16V9.8l-8 5.2z" fill-rule="evenodd"/></svg>
          </span>
          <span>tobias@larvik.nz</span>
        </li>
      </ul>
    </div>
  </section>

  <section class="card-back" aria-label="Business card, back">
    <div class="panel-texture" role="img" aria-label="Blue background with soft curved globe lines"></div>
    <div class="back-brand">
      <div class="brand-dot brand-dot--back" aria-hidden="true"></div>
      <div class="brand-name brand-name--back">LARVIK CONSULTING</div>
    </div>
    <p class="website">www.larvikconsulting.nz</p>
  </section>

</main>
</body>
</html>
```